Business card design for engineering firm specializing in defense industry.

We need a professional business card design. Something simple but stands out. We are an engineering company specializing in composites in the defense industry.
Industry/Entity Type
Defense
Contact Information for Business Card
A simple black business card with the Varlonix yellow color is what we had in mind but open for other designs.
Colors
ffc214

```html
<!DOCTYPE html>
<html lang="en">
<head>
<meta charset="utf-8">
<title>Varlonix Business Card</title>
<link rel="stylesheet" href="https://fonts.googleapis.com/css2?family=Archivo:wght@400;700;800&display=swap">
<style>
  :root {
    --bg: #1b1c1f;
    --card: #232528;
    --card-edge: #2c2e32;
    --brand-yellow: #ffc214;
    --line-gold: #b8922a;
    --white: #ffffff;
    --muted: #d9d9d9;
    --emboss: #3d4045;
  }
  * { box-sizing: border-box; margin: 0; padding: 0; }
  html, body { width: 1200px; height: 800px; overflow: hidden; background: var(--bg); }
  body { font-family: "Archivo", Arial, sans-serif; color: var(--white); position: relative; }

  .card {
    position: absolute;
    background: var(--card);
    border-radius: 18px;
    border: 1px solid var(--card-edge);
    box-shadow: 0 20px 40px rgba(0,0,0,0.55);
    overflow: hidden;
  }

  /* Front */
  .card-front { left: 90px; top: 250px; width: 525px; height: 300px; display: flex; align-items: center; justify-content: center; }
  .front-wordmark { font-size: 64px; font-weight: 800; color: var(--emboss); letter-spacing: 1px; }

  /* Back */
  .card-back { left: 740px; top: 137px; width: 300px; height: 525px; }
  .back-wordmark { position: absolute; top: 46px; left: 0; right: 0; text-align: center; font-size: 40px; font-weight: 800; color: var(--white); letter-spacing: 0.5px; }
  .brand-mark { display: inline-block; width: 12px; height: 12px; background: var(--brand-yellow); margin-left: 8px; vertical-align: middle; }

  .person { position: absolute; top: 150px; left: 0; right: 0; text-align: center; }
  .person-name { font-size: 20px; font-weight: 800; letter-spacing: 0.5px; }
  .person-role { font-size: 15px; color: var(--brand-yellow); margin-top: 2px; }

  .divider { position: absolute; left: 30px; right: 30px; height: 1px; background: var(--line-gold); }
  .divider-top { top: 222px; }
  .divider-bottom { top: 350px; }

  .contact-list { position: absolute; top: 240px; left: 30px; right: 30px; list-style: none; }
  .contact-item { display: flex; align-items: center; gap: 12px; font-size: 15px; color: var(--muted); margin-bottom: 14px; }
  .contact-icon { width: 26px; height: 26px; flex: none; }

  .address { position: absolute; top: 368px; left: 30px; right: 30px; font-size: 15px; line-height: 1.45; color: var(--muted); }

  .web-band { position: absolute; left: 0; right: 0; bottom: 0; height: 62px; background: var(--brand-yellow); border-top: 5px solid var(--white); box-shadow: 0 -6px 0 var(--card); display: flex; align-items: center; justify-content: center; }
  .web-address { font-size: 16px; color: var(--bg); letter-spacing: 0.5px; }
</style>
</head>
<body>
  <section class="card card-front" aria-label="Card front">
    <span class="front-wordmark">Varlonix</span>
  </section>

  <section class="card card-back" aria-label="Card back">
    <div class="back-wordmark">Varlonix<span class="brand-mark"></span></div>

    <div class="person">
      <div class="person-name">DARA KELLNER</div>
      <div class="person-role">President</div>
    </div>

    <div class="divider divider-top"></div>

    <ul class="contact-list">
      <li class="contact-item">
        <svg class="contact-icon" viewBox="0 0 26 26" aria-hidden="true">
          <circle cx="13" cy="13" r="12" fill="#ffc214" stroke="#232528" stroke-width="1"/>
          <rect x="8.5" y="8" width="9" height="10" rx="1.5" fill="none" stroke="#232528" stroke-width="1.6"/>
          <line x1="11" y1="16" x2="15" y2="16" stroke="#232528" stroke-width="1.2"/>
        </svg>
        <span>555-014-2290</span>
      </li>
      <li class="contact-item">
        <svg class="contact-icon" viewBox="0 0 26 26" aria-hidden="true">
          <circle cx="13" cy="13" r="12" fill="#ffc214" stroke="#232528" stroke-width="1"/>
          <rect x="7.5" y="9" width="11" height="8" fill="none" stroke="#232528" stroke-width="1.5"/>
          <polyline points="7.5,9 13,13.5 18.5,9" fill="none" stroke="#232528" stroke-width="1.5"/>
        </svg>
        <span>info@varlonixmail.com</span>
      </li>
    </ul>

    <div class="divider divider-bottom"></div>

    <p class="address">PO BOX 48 Harlow Road<br>4th street Ashbury</p>

    <div class="web-band">
      <span class="web-address">www.VARLONIXWEB.com</span>
    </div>
  </section>
</body>
</html>
```